Envelope Design Project

I will need two envelopes to be designed:-

DL size
C4 size

Please see uploaded documents for Design specs:

1) Design specs provided by printer (doc called DL Envelope Specs)
2) Design specs to comply with Kestrel Mailways requirements (doc called Kestrel Mailways Envelope Design Requirements)

Please adhere to the above for final design. Many thanks.

Target Market(s)

Real Estate Agents, Strata Managers, Builders, Architects, Business Owners

Industry/Entity Type

Printer

Requirements
Must have
• In top left corner
- Logo
- Return address - Suite 5, 19 Wattlebark Rd, Marrowick, NSW 2417

```html
<!DOCTYPE html>
<html lang="en">
<head>
<meta charset="utf-8">
<title>Corvane Asbestos &amp; Safety – Envelope Set</title>
<link rel="stylesheet" href="https://fonts.googleapis.com/css2?family=Didact+Gothic&display=swap">
<style>
  :root {
    --backdrop: #e9e7e3;
    --paper: #ffffff;
    --paper-shade: #ededed;
    --navy: #1f1d3d;
    --green: #8cb033;
    --green-deep: #6c8a25;
    --text: #2b2b2b;
  }
  * { box-sizing: border-box; margin: 0; padding: 0; }
  html, body {
    width: 1200px;
    height: 900px;
    overflow: hidden;
    background: var(--backdrop);
    font-family: "Didact Gothic", "Century Gothic", sans-serif;
  }
  .canvas {
    position: relative;
    width: 1200px;
    height: 900px;
  }
  .envelope {
    position: absolute;
    background: linear-gradient(160deg, var(--paper) 0%, var(--paper) 45%, var(--paper-shade) 100%);
    box-shadow: 0 6px 18px rgba(0, 0, 0, 0.18);
    overflow: hidden;
  }
  .envelope--dl {
    left: 110px;
    top: 110px;
    width: 460px;
    height: 230px;
  }
  .envelope--c4 {
    left: 470px;
    top: 300px;
    width: 640px;
    height: 452px;
  }
  .envelope__band {
    position: absolute;
    left: 0;
    right: 0;
    bottom: 0;
    background: linear-gradient(90deg, var(--green) 0%, var(--green) 60%, var(--green-deep) 100%);
  }
  .envelope--dl .envelope__band { height: 28px; }
  .envelope--c4 .envelope__band { height: 62px; }

  .sender {
    position: absolute;
    color: var(--navy);
  }
  .envelope--dl .sender { left: 26px; top: 26px; }
  .envelope--c4 .sender { left: 58px; top: 58px; }

  .brand {
    display: flex;
    align-items: center;
    gap: 8px;
  }
  .brand__mark {
    display: block;
    border: 3px solid var(--navy);
    border-radius: 4px;
  }
  .envelope--dl .brand__mark { width: 20px; height: 20px; border-width: 2px; }
  .envelope--c4 .brand__mark { width: 34px; height: 34px; }

  .brand__text {
    display: flex;
    flex-direction: column;
    line-height: 1;
    color: var(--navy);
  }
  .brand__name { letter-spacing: 0.5px; }
  .brand__tagline { letter-spacing: 0.6px; }
  .envelope--dl .brand__name { font-size: 20px; }
  .envelope--dl .brand__tagline { font-size: 7px; margin-top: 2px; }
  .envelope--c4 .brand__name { font-size: 34px; }
  .envelope--c4 .brand__tagline { font-size: 11.5px; margin-top: 3px; }

  .sender__address {
    color: var(--text);
    white-space: nowrap;
  }
  .envelope--dl .sender__address { font-size: 7px; margin-top: 6px; }
  .envelope--c4 .sender__address { font-size: 10px; margin-top: 10px; }
</style>
</head>
<body>
  <main class="canvas">
    <section class="envelope envelope--dl" aria-label="DL envelope">
      <div class="sender">
        <div class="brand">
          <span class="brand__mark"></span>
          <div class="brand__text">
            <span class="brand__name">Corvane</span>
            <span class="brand__tagline">ASBESTOS &amp; SAFETY</span>
          </div>
        </div>
        <p class="sender__address">Suite 5, 19 Wattlebark Rd, Marrowick, NSW 2417</p>
      </div>
      <div class="envelope__band"></div>
    </section>

    <section class="envelope envelope--c4" aria-label="C4 envelope">
      <div class="sender">
        <div class="brand">
          <span class="brand__mark"></span>
          <div class="brand__text">
            <span class="brand__name">Corvane</span>
            <span class="brand__tagline">ASBESTOS &amp; SAFETY</span>
          </div>
        </div>
        <p class="sender__address">Suite 5, 19 Wattlebark Rd, Marrowick, NSW 2417</p>
      </div>
      <div class="envelope__band"></div>
    </section>
  </main>
</body>
</html>
```